Bellhaven Select Business Card Design Project

About the company: Here at Marigrove Essence, we focus on cosmetic products that based on essential oils and different kinds of plant essences. All of our raw materials are pure organic and specially selected from local producers in Australia.

I'm here to look for a unique business card design, to replace the current one later on, so I don't have many requirements. Why I wanna restrict designers' creativity?

All I know is: 1. do not make it too complicated, straight forward, simple and pure. 2. this design may be used for other purposes (i.e. logo and slogan on the front, Brand Story and contact details at the back). Therefor, I'd like to have the design for 3 layouts, one only have logo, slogan, contact detials, one for the brand story, the other one for the personal business card with staff's mob etc...

A vector graphic is required, i.e. eps, ai, easy for me to resize.

Round Corner.

Thanks
Updates

Plz add "Hand made in Australia" in the design, cheers.

Target Market(s)

Women aged yr 20-50

Industry/Entity Type

Business

Requirements
Must have
• Logo: please see attacment (eps, ai)

Slogan: Dew Touched Delight

Website:www.marigroveessence-demo.com.au

Address: temporary not available

Phone: temporary not available

"Hand made in Australia"

Nice to have
• Prefer round corner

```html
<!DOCTYPE html>
<html lang="en">
<head>
<meta charset="utf-8">
<title>Marigrove Essence – Business Card</title>
<link rel="stylesheet" href="https://fonts.googleapis.com/css2?family=Jost:ital,wght@0,400;0,500;1,500&display=swap">
<style>
  :root {
    --canvas: #ffffff;
    --cream: #fdfbd0;
    --lime: #d5f671;
    --lime-bright: #b4ec16;
    --brand-pink: #e0307f;
    --rose-pink: #f06aa8;
    --ink: #111111;
  }
  * { margin: 0; padding: 0; box-sizing: border-box; }
  html, body {
    width: 1200px;
    height: 1200px;
    overflow: hidden;
    background: var(--canvas);
    font-family: "Jost", "Helvetica Neue", Arial, sans-serif;
    color: var(--ink);
  }
  .canvas { position: relative; width: 1200px; height: 1200px; }
  .card {
    position: absolute;
    left: 78px;
    top: 303px;
    width: 1044px;
    height: 594px;
    border-radius: 42px;
    overflow: hidden;
    background: var(--cream);
  }
  .card-bands { position: absolute; inset: 0; width: 100%; height: 100%; }
  .brand {
    position: absolute;
    left: 0;
    width: 100%;
    top: 48px;
    display: flex;
    justify-content: center;
  }
  .brand-name {
    font-weight: 500;
    font-size: 82px;
    line-height: 1;
    color: var(--brand-pink);
    letter-spacing: 1px;
    white-space: nowrap;
  }
  .brand-mark {
    position: absolute;
    left: 356px;
    top: 207px;
    width: 134px;
    height: 134px;
    border-radius: 50%;
    background: var(--rose-pink);
  }
  .slogan {
    position: absolute;
    left: 549px;
    top: 284px;
    font-size: 37px;
    font-style: italic;
    font-weight: 500;
    line-height: 1;
    white-space: nowrap;
  }
  .contact {
    position: absolute;
    left: 50px;
    top: 330px;
    list-style: none;
    font-size: 35px;
    line-height: 47px;
  }
  .made-in, .website {
    position: absolute;
    right: 0;
    line-height: 1;
    white-space: nowrap;
  }
  .made-in { top: 494px; right: 146px; font-size: 37px; }
  .website { top: 541px; right: 62px; font-size: 34px; }
</style>
</head>
<body>
<main class="canvas">
  <section class="card" aria-label="Marigrove Essence business card">
    <svg class="card-bands" viewBox="0 0 1044 594" preserveAspectRatio="none" aria-hidden="true">
      <path d="M0,152 Q500,330 1044,256 L1044,594 L0,594 Z" fill="var(--lime-bright)"/>
      <path d="M0,186 Q500,352 1044,288 L1044,594 L0,594 Z" fill="var(--lime)"/>
    </svg>

    <div class="brand">
      <span class="brand-name">Marigrove Essence</span>
    </div>
    <span class="brand-mark" aria-hidden="true"></span>

    <p class="slogan">Dew Touched Delight</p>

    <ul class="contact">
      <li>Name:&nbsp; (here)</li>
      <li>Address: (here)</li>
      <li>Phone: xxx.xxx.xxxx</li>
    </ul>

    <p class="made-in">Hand made in Australia</p>
    <p class="website">www.marigroveessence-demo.com.au</p>
  </section>
</main>
</body>
</html>
```